Business Cards

Business cards (double-sided) to be handed out to clients and potential clients, with contact details, logo .

Target Market(s)

Small to medium size businesses

Industry/Entity Type

Accountants

Contact Information for Business Card

Brightwater Ledger & Counsel Ltd

Colors

Designer to choose only greyscale colors for use in the design.

Requirements
Must have
• Name, Title, Address, Phone number, Email, Website
Nice to have
• Modern, clean lines, classy
Should not have
• Business cards to be double-sided. Form keeps reverting to single-sided.

```html
<!DOCTYPE html>
<html lang="en">
<head>
<meta charset="utf-8">
<title>Brightwater Ledger &amp; Counsel – Business Cards</title>
<link href="https://fonts.googleapis.com/css2?family=Lato:wght@400;700&display=swap" rel="stylesheet">
<style>
  :root {
    --backdrop: #2b2e30;
    --card-front: #767676;
    --card-back: #ffffff;
    --ink: #111111;
    --ink-soft: #555555;
    --rule: #4a4a4a;
    --foil: #ececec;
    --band-dark: #0d0d0d;
    --band-grey: #8a8a8a;
  }
  * { box-sizing: border-box; margin: 0; padding: 0; }
  html, body { width: 1200px; height: 1200px; overflow: hidden; }
  body {
    background: var(--backdrop);
    font-family: "Lato", sans-serif;
    position: relative;
  }
  .card {
    position: absolute;
    left: 150px;
    width: 900px;
    height: 514px;
    overflow: hidden;
    box-shadow: 0 18px 40px rgba(0,0,0,0.45);
  }
  .card--front { top: 60px; background: var(--card-front); }
  .card--back { top: 626px; background: var(--card-back); color: var(--ink); }

  .front-wordmark {
    position: absolute; inset: 0;
    display: flex; align-items: center; justify-content: center;
    font-weight: 400; font-size: 78px; letter-spacing: 10px;
    color: var(--foil); text-transform: uppercase;
  }

  .back-wordmark {
    position: absolute; top: 62px; right: 60px;
    font-weight: 400; font-size: 38px; letter-spacing: 5px;
    text-transform: uppercase; color: var(--ink);
  }
  .main-rule {
    position: absolute; left: 60px; right: 60px; top: 232px;
    height: 2px; background: var(--rule);
  }
  .company {
    position: absolute; right: 60px; top: 252px;
    text-align: right; color: var(--ink-soft);
    font-size: 18px; line-height: 1.45;
  }
  .company__name { font-weight: 700; font-size: 20px; color: #333; }

  .person { position: absolute; left: 60px; top: 288px; }
  .person__name {
    font-weight: 700; font-size: 34px; letter-spacing: 1.5px;
    text-transform: uppercase; line-height: 1.1;
  }
  .person__title { font-size: 19px; color: var(--ink-soft); margin-top: 2px; }
  .person__rule { width: 300px; height: 2px; background: var(--rule); margin: 12px 0 10px; }
  .contacts { list-style: none; font-size: 19px; color: var(--ink-soft); }
  .contacts li { display: flex; align-items: center; gap: 14px; height: 29px; }
  .contacts svg { width: 15px; height: 15px; fill: var(--ink); flex: none; }

  .bands { position: absolute; left: 0; bottom: 0; width: 900px; height: 80px; }
</style>
</head>
<body>
  <section class="card card--front" aria-label="Card front">
    <div class="front-wordmark">Brightwater</div>
  </section>

  <section class="card card--back" aria-label="Card back">
    <div class="back-wordmark">Brightwater</div>
    <div class="main-rule"></div>

    <address class="company" style="font-style:normal">
      <div class="company__name">Brightwater Ledger &amp; Counsel Ltd</div>
      <div>Street address, City</div>
      <div>State &amp; ZIP code Country</div>
    </address>

    <div class="person">
      <div class="person__name">Daniel Harlow</div>
      <div class="person__title">Founder &amp; CEO</div>
      <div class="person__rule"></div>
      <ul class="contacts">
        <li>
          <svg viewBox="0 0 16 16" aria-hidden="true"><path d="M3.5 1.5l2.4 2.6-1.3 1.9c.9 2 2.4 3.5 4.4 4.4l1.9-1.3 2.6 2.4-1.3 2.3C7.3 13.6 2.4 8.7 1.2 2.8z"/></svg>
          321-555-0148
        </li>
        <li>
          <svg viewBox="0 0 16 16" aria-hidden="true"><path d="M1 3h14v10H1z M2.5 4.5L8 9l5.5-4.5" fill="none" stroke="#111" stroke-width="1.6"/></svg>
          daniel@BrightwaterLedger.com
        </li>
        <li>
          <svg viewBox="0 0 16 16" aria-hidden="true"><circle cx="8" cy="8" r="7"/><path d="M1 8h14M8 1c-3 3.5-3 10.5 0 14M8 1c3 3.5 3 10.5 0 14" fill="none" stroke="#fff" stroke-width="1"/></svg>
          BrightwaterLedger.com
        </li>
      </ul>
    </div>

    <svg class="bands" viewBox="0 0 900 80" aria-hidden="true">
      <polygon points="0,58 600,58 592,80 0,80" fill="var(--band-dark)"/>
      <polygon points="625,6 900,6 900,80 598,80" fill="var(--band-grey)"/>
    </svg>
  </section>
</body>
</html>
```